Package design for small honey and vegetable farm

I would like to have a unique design for the packaging of our honey and vegetables. I have attached the logo from our farm "Willowbrook Acres" that should be on the packaging for both the honey and the vegetables

For the honey the writing, "100% pure organic honey" must be on the packaging in some place. As well as "from the busy bees at Willowbrook Acres". I have attached some designs that I like.

For the vegetables. The design will need to go on a box like the one in the attached image. The phrase "Organically Grown" should be on the package. I would like the background color of the package to be black. I think I would also like to see some stylized vegetables (tomatoes in particular) on the package.

I would like to be able to get all the colors (RGB) used in the designs so I can pass them on to printers.

Industry/Entity Type

Farm

Colors
fbee3e

Requirements
Must have
• For the honey, the package it must say "100% pure organic honey".
• For the vegetables I would like the background color to be black. I would also like some stylized vegetables (tomatoes in particular) added to the package.

```html
<!DOCTYPE html>
<html lang="en">
<head>
<meta charset="utf-8">
<title>Willowbrook Acres – Honey Labels</title>
<link rel="stylesheet" href="https://fonts.googleapis.com/css2?family=Montserrat:wght@400;500;600&display=swap">
<style>
  :root {
    --honey: #fbee3e;
    --honey-deep: #e8d80a;
    --gold-text: #d9c400;
    --paper: #f7f7f5;
    --ink: #1c1c1c;
    --backdrop: #e9ecec;
  }
  * { margin: 0; padding: 0; box-sizing: border-box; }
  html, body { width: 1200px; height: 675px; overflow: hidden; }
  body {
    background: var(--backdrop);
    font-family: "Montserrat", sans-serif;
    position: relative;
  }
  .set { position: absolute; top: 120px; display: flex; flex-direction: column; align-items: center; }
  .set--left { left: 190px; width: 180px; }
  .set--center { left: 490px; width: 220px; top: 80px; }
  .set--right { left: 800px; width: 240px; top: 140px; }

  /* neck band with hanging tag */
  .neck { position: relative; height: 44px; width: 66px; background: var(--paper); margin-bottom: 34px; }
  .neck--yellow { background: var(--honey-deep); width: 76px; height: 52px; }
  .tag {
    position: absolute; left: 66px; top: -4px;
    width: 150px; height: 48px;
    background: var(--paper);
    display: flex; flex-direction: column; justify-content: center; align-items: flex-end;
    padding: 0 12px; gap: 4px;
  }
  .neck--yellow .tag { left: 76px; width: 100px; height: 46px; top: -4px; background: var(--honey-deep); align-items: flex-start; padding: 0 10px; }
  .tag__line { font-size: 5px; letter-spacing: 0.12em; text-transform: uppercase; color: #9a9a9a; font-weight: 600; }
  .tag__line b { color: var(--gold-text); font-weight: 600; }
  .tag__big { font-size: 8.5px; letter-spacing: 0.16em; text-transform: uppercase; color: #fff; font-weight: 500; line-height: 1.4; }
  .tag__brand { font-size: 6px; color: var(--gold-text); font-weight: 500; }

  /* main labels */
  .label { position: relative; width: 100%; display: flex; flex-direction: column; background: var(--paper); }
  .label--scalloped::before, .label--scalloped::after {
    content: ""; position: absolute; left: 0; right: 0; height: 6px;
    background: radial-gradient(circle at 50% 0, transparent 3px, var(--paper) 3.5px) 0 0 / 8px 6px repeat-x;
  }
  .label--scalloped::before { top: -6px; transform: scaleY(-1); }
  .label--scalloped::after { bottom: -6px; }

  .label__brand-area { display: flex; align-items: center; justify-content: center; gap: 6px; }
  .brand { font-weight: 500; font-size: 15px; letter-spacing: 0.02em; color: var(--gold-text); }
  .brand-dot { width: 9px; height: 9px; border-radius: 50%; background: var(--gold-text); }
  .label__claim {
    background: var(--honey-deep); color: #fff;
    display: flex; align-items: center; justify-content: center;
    font-size: 7px; letter-spacing: 0.2em; text-transform: uppercase; font-weight: 500;
  }
  .label__origin {
    background: var(--ink); color: #fff;
    display: flex; align-items: center; justify-content: center;
    font-size: 4.5px; letter-spacing: 0.14em; text-transform: uppercase; font-weight: 500;
  }

  .set--left .label__brand-area { height: 150px; }
  .set--left .label__claim { height: 46px; }
  .set--left .label__origin { height: 20px; }
  .set--left .label__foot { height: 22px; }

  .set--right .label__brand-area { height: 110px; }
  .set--right .label__claim { height: 44px; }
  .set--right .label__origin { height: 20px; }
  .set--right .label__foot { height: 14px; }

  .label--wrap { background: var(--honey-deep); }
  .label--wrap .label__brand-area { height: 210px; }
  .label--wrap .brand { color: var(--ink); font-size: 17px; }
  .label--wrap .brand-dot { background: var(--ink); }
  .label--wrap .label__claim { background: var(--paper); color: var(--gold-text); height: 58px; font-size: 8px; }
  .label--wrap .label__origin { height: 26px; font-size: 5px; }
  .label--wrap .label__foot { height: 62px; }
</style>
</head>
<body>
  <section class="set set--left">
    <div class="neck">
      <div class="tag">
        <span class="tag__line">100% pure <b>organic honey</b> from</span>
        <span class="tag__brand">Willowbrook Acres</span>
      </div>
    </div>
    <div class="label label--scalloped">
      <div class="label__brand-area"><span class="brand-dot"></span><span class="brand">Willowbrook Acres</span></div>
      <div class="label__claim">100% pure organic honey</div>
      <div class="label__origin">from the busy bees at Willowbrook Acres</div>
      <div class="label__foot"></div>
    </div>
  </section>

  <section class="set set--center">
    <div class="neck neck--yellow">
      <div class="tag">
        <span class="tag__big">100% pure<br>organic honey</span>
      </div>
    </div>
    <div class="label label--wrap">
      <div class="label__brand-area"><span class="brand-dot"></span><span class="brand">Willowbrook Acres</span></div>
      <div class="label__claim">100% pure organic honey</div>
      <div class="label__origin">from the busy bees at Willowbrook Acres</div>
      <div class="label__foot"></div>
    </div>
  </section>

  <section class="set set--right">
    <div class="neck" style="width:92px">
      <div class="tag" style="left:92px;width:104px;height:56px;align-items:flex-start">
        <span class="tag__line"><b>100% pure<br>organic honey</b><br>from</span>
        <span class="tag__brand">Willowbrook Acres</span>
      </div>
    </div>
    <div class="label label--scalloped">
      <div class="label__brand-area"><span class="brand-dot"></span><span class="brand">Willowbrook Acres</span></div>
      <div class="label__claim">100% pure organic honey</div>
      <div class="label__origin">from the busy bees at Willowbrook Acres</div>
      <div class="label__foot"></div>
    </div>
  </section>
</body>
</html>
```